ORVALIS MED -DIAGNOSTIC CENTRE FOR IMAGES

Our Activity provides diagnostic services for images (RMI, Tac, RX, Ultrasound etc.)
We would like to create a broschure that illustrates our services.
We would like to give maximum attention to the Diagnostic service dedicated to "HEART", therefore maximum evidence to the world of Cardiology.
In the background we would like to highlight the other diagnostic services dedicated to the Rest of the Body (Brain, Knees Legs etc.)
Target Market(s)
PERSONS WHO NEED TO PERFORM DIAGNOSTIC TESTS (MRI, CT, ULTRASOUND, RX ETC.)
Industry/Entity Type
HEALTH
Requirements
Must have
- The company logo, must have diagnostic images (MRI, CT, X-ray, ultrasound), must be simple and intuitive, which is harmonious with the colors of our company logo
Should not have
- Colours that are not in harmony with our company logo

```html
<!DOCTYPE html>
<html lang="en">
<head>
<meta charset="utf-8">
<title>Orvalis Med – Cardiology &amp; Diagnostics Brochure</title>
<link href="https://fonts.googleapis.com/css2?family=Inter:wght@400;500;600;700;800&display=swap" rel="stylesheet">
<style>
  :root {
    --navy: #0c3457;
    --teal: #16b2a3;
    --ink: #0f3a5c;
    --dark-panel: #121212;
    --ice: #e4f4fb;
    --steel: #c3ced4;
    --white: #ffffff;
  }
  * { margin: 0; padding: 0; box-sizing: border-box; }
  html, body { width: 1200px; height: 842px; overflow: hidden; background: var(--white); }
  body { font-family: "Inter", sans-serif; color: var(--ink); }
  .page { position: relative; width: 1200px; height: 842px; overflow: hidden; background: var(--white); }
  .abs { position: absolute; }

  /* decorations */
  .corner-tile { left: 0; top: 0; width: 62px; height: 41px; background: var(--ice); border-bottom-right-radius: 12px; }
  .outline-tab { border: 2px solid var(--navy); border-radius: 12px; }
  .outline-tab.top { left: 29px; top: -14px; width: 113px; height: 28px; }
  .outline-tab.bottom { left: 1040px; top: 808px; width: 113px; height: 50px; }
  .bar { background: var(--navy); border-radius: 7px; }
  .bar.top { left: 998px; top: 21px; width: 220px; height: 13px; }
  .bar.bottom { left: -10px; top: 809px; width: 212px; height: 13px; }
  .soft-cross { background: var(--ice); border-radius: 8px; }
  .steel-tile { left: 1108px; top: 751px; width: 110px; height: 110px; background: var(--steel); border-top-left-radius: 26px; }
  .ice-strip { left: 1108px; top: 795px; width: 92px; height: 47px; background: var(--ice); }

  /* headings */
  .heading { font-weight: 800; font-size: 28.5px; line-height: 36px; letter-spacing: -0.2px; }
  .heading .kicker { color: var(--navy); display: block; }
  .heading .title { color: var(--teal); display: block; }
  .intro { font-size: 14.6px; line-height: 20px; color: var(--navy); }

  /* service list */
  .service { left: 254px; width: 306px; }
  .label {
    display: inline-block; background: var(--teal); color: var(--white);
    font-weight: 700; font-size: 17px; line-height: 25px; padding: 0 9px; border-radius: 3px;
  }
  .service p { font-size: 14.3px; line-height: 17.2px; color: var(--navy); text-align: justify; margin-top: 1px; }

  .benefits-title { left: 254px; top: 713px; font-weight: 700; font-size: 17px; color: var(--navy); }
  .pill {
    background: var(--teal); color: var(--white); font-size: 14.6px; line-height: 26px;
    padding: 0 12px; border-radius: 5px; white-space: nowrap;
  }

  /* photo areas */
  .photo { border-radius: 4px; }
  .photo.ultrasound { left: 36px; top: 277px; width: 198px; height: 238px; background: linear-gradient(160deg, #2b3440 0%, #8c949c 55%, #e9ecee 100%); }
  .photo.xray { left: 37px; top: 539px; width: 175px; height: 230px; background: linear-gradient(180deg, #f3f5f6 0%, #dfe3e6 60%, #f5f6f7 100%); }
  .photo.ct { left: 630px; top: 272px; width: 293px; height: 191px; background: radial-gradient(ellipse at 40% 45%, #f4f7f8 0%, #e3e8ea 60%, #f7f9fa 100%); }

  .tag {
    background: var(--teal); color: var(--white); font-size: 14.6px; line-height: 26px;
    padding: 0 12px; border-radius: 5px; white-space: nowrap; font-weight: 500;
  }

  /* dark benefits panel */
  .panel { left: 621px; top: 520px; width: 554px; height: 275px; background: var(--dark-panel); border-radius: 25px; }
  .check-item { display: flex; gap: 8px; color: var(--white); font-size: 14.6px; line-height: 17px; font-weight: 500; }
  .check-item svg { flex: none; margin-top: 2px; }
</style>
</head>
<body>
<div class="page">

  <!-- background decorations -->
  <div class="abs corner-tile"></div>
  <div class="abs outline-tab top"></div>
  <div class="abs bar top"></div>
  <div class="abs bar bottom"></div>
  <div class="abs soft-cross" style="left:685px;top:-10px;width:37px;height:107px;"></div>
  <div class="abs soft-cross" style="left:636px;top:24px;width:134px;height:60px;"></div>
  <div class="abs soft-cross" style="left:429px;top:777px;width:62px;height:20px;border-radius:5px;"></div>
  <div class="abs soft-cross" style="left:449px;top:766px;width:18px;height:52px;border-radius:5px;"></div>
  <div class="abs steel-tile"></div>
  <div class="abs ice-strip"></div>
  <div class="abs outline-tab bottom"></div>

  <svg class="abs" style="left:525px;top:41px" width="23" height="23" viewBox="0 0 23 23">
    <g stroke="#0c3457" stroke-width="1.6" stroke-linecap="round">
      <line x1="11.5" y1="1" x2="11.5" y2="8"/><line x1="11.5" y1="15" x2="11.5" y2="22"/>
      <line x1="1" y1="11.5" x2="8" y2="11.5"/><line x1="15" y1="11.5" x2="22" y2="11.5"/>
    </g>
  </svg>

  <svg class="abs" style="left:1139px;top:50px" width="48" height="48" viewBox="0 0 48 48">
    <rect x="0" y="18" width="28" height="28" rx="5" fill="#16b2a3"/>
    <g fill="#0c3457">
      <circle cx="11" cy="2" r="1.3"/><circle cx="20" cy="2" r="1.3"/><circle cx="29" cy="2" r="1.3"/><circle cx="38" cy="2" r="1.3"/><circle cx="46" cy="2" r="1.3"/>
      <circle cx="11" cy="12" r="1.3"/><circle cx="20" cy="12" r="1.3"/><circle cx="29" cy="12" r="1.3"/><circle cx="38" cy="12" r="1.3"/><circle cx="46" cy="12" r="1.3"/>
      <circle cx="11" cy="24" r="1.3"/><circle cx="20" cy="24" r="1.3"/><circle cx="38" cy="24" r="1.3"/><circle cx="46" cy="24" r="1.3"/>
      <circle cx="11" cy="35" r="1.3"/><circle cx="20" cy="35" r="1.3"/><circle cx="38" cy="35" r="1.3"/><circle cx="46" cy="35" r="1.3"/>
    </g>
  </svg>

  <!-- left column: cardiology -->
  <h1 class="abs heading" style="left:36px;top:48px;">
    <span class="kicker">OUR MAIN FOCUS</span>
    <span class="title">CARDIOLOGY EXCELLENCE</span>
  </h1>
  <p class="abs intro" style="left:36px;top:134px;width:550px;">
    At Orvalis Med, we are dedicated to delivering exceptional cardiac care to safeguard your heart health. Our cutting-edge technology and skilled medical professionals are committed to providing you with accurate diagnoses and effective treatments, ensuring your heart remains in the best possible condition.
  </p>

  <div class="abs photo ultrasound" role="img" aria-label="Cardiac ultrasound workstation with a magnified echo scan"></div>
  <div class="abs photo xray" role="img" aria-label="Digital X-ray system with table and wall stand"></div>

  <section class="abs service" style="top:254px;">
    <span class="label">Cardiac Imaging</span>
    <p>We offer advanced cardiac imaging services, including state-of-the-art MRI and CT scans, to provide a comprehensive view of your heart's structure and function</p>
  </section>
  <section class="abs service" style="top:368px;">
    <span class="label">Electrocardiography (ECG/EKG)</span>
    <p>Our ECG/EKG tests accurately monitor your heart's electrical activity, helping to diagnose arrhythmias, heart attacks, and other cardiac conditions.</p>
  </section>
  <section class="abs service" style="top:485px;width:310px;">
    <span class="label">Echocardiography</span>
    <p>Our high-resolution echocardiography allows us to assess your heart's chambers, valves, and blood flow, aiding in the detection of heart diseases.</p>
  </section>
  <section class="abs service" style="top:602px;">
    <span class="label">Holter Monitoring</span>
    <p>For continuous heart monitoring, our Holter monitors record your heart's activity over 24 hours or more, helping us identify irregularities that may go unnoticed in shorter tests.</p>
  </section>

  <h2 class="abs benefits-title">Other Benefits</h2>
  <span class="abs pill" style="left:253px;top:737px;">Stress Testing</span>
  <span class="abs pill" style="left:385px;top:737px;">Coronary Angiography</span>
  <span class="abs pill" style="left:253px;top:772px;">Cardiac Consultations</span>

  <!-- right column: other diagnostics -->
  <h1 class="abs heading" style="left:625px;top:48px;">
    <span class="kicker">COMPREHENSIVE DIAGNOSTICS</span>
    <span class="title">BEYOND CARDIOLOGY</span>
  </h1>
  <p class="abs intro" style="left:626px;top:134px;width:550px;">
    In addition to our specialized cardiology services, we offer a wide range of comprehensive diagnostic services to address your healthcare needs holistically. At [Your Company Name], we believe in the importance of thorough diagnostics to ensure your overall well-being. Our diagnostic services include:
  </p>

  <div class="abs photo ct" role="img" aria-label="CT scanner gantry with patient table"></div>

  <span class="abs tag" style="left:940px;top:269px;">Neuroimaging</span>
  <span class="abs tag" style="left:1075px;top:269px;">Ultrasound</span>
  <span class="abs tag" style="left:940px;top:308px;">Musculoskeletal Imaging</span>
  <span class="abs tag" style="left:940px;top:347px;">Abdominal Imaging</span>
  <span class="abs tag" style="left:940px;top:386px;">Multi-Specialty Consultations</span>
  <span class="abs tag" style="left:940px;top:424px;">X-rays (RX)</span>

  <div class="abs panel"></div>

  <div class="abs check-item" style="left:648px;top:550px;"><svg width="14" height="12" viewBox="0 0 14 12"><path d="M1 6.5 5 10.5 13 1.5" fill="none" stroke="#16b2a3" stroke-width="2.6" stroke-linecap="round" stroke-linejoin="round"/></svg><span>Enhanced treatment planning<br>for cardiac conditions.</span></div>
  <div class="abs check-item" style="left:648px;top:608px;"><svg width="14" height="12" viewBox="0 0 14 12"><path d="M1 6.5 5 10.5 13 1.5" fill="none" stroke="#16b2a3" stroke-width="2.6" stroke-linecap="round" stroke-linejoin="round"/></svg><span>Personalized care for<br>better patient outcomes.</span></div>
  <div class="abs check-item" style="left:648px;top:670px;"><svg width="14" height="12" viewBox="0 0 14 12"><path d="M1 6.5 5 10.5 13 1.5" fill="none" stroke="#16b2a3" stroke-width="2.6" stroke-linecap="round" stroke-linejoin="round"/></svg><span>Enhanced treatment planning<br>for cardiac conditions.</span></div>
  <div class="abs check-item" style="left:648px;top:724px;"><svg width="14" height="12" viewBox="0 0 14 12"><path d="M1 6.5 5 10.5 13 1.5" fill="none" stroke="#16b2a3" stroke-width="2.6" stroke-linecap="round" stroke-linejoin="round"/></svg><span>Enhanced detection and<br>localization of cardiac issues.</span></div>

  <div class="abs check-item" style="left:922px;top:550px;"><svg width="14" height="12" viewBox="0 0 14 12"><path d="M1 6.5 5 10.5 13 1.5" fill="none" stroke="#16b2a3" stroke-width="2.6" stroke-linecap="round" stroke-linejoin="round"/></svg><span>Cutting-edge technology<br>for precise imaging.</span></div>
  <div class="abs check-item" style="left:922px;top:608px;"><svg width="14" height="12" viewBox="0 0 14 12"><path d="M1 6.5 5 10.5 13 1.5" fill="none" stroke="#16b2a3" stroke-width="2.6" stroke-linecap="round" stroke-linejoin="round"/></svg><span>Comprehensive fusion of PET<br>and CT scans.</span></div>
  <div class="abs check-item" style="left:922px;top:670px;"><svg width="14" height="12" viewBox="0 0 14 12"><path d="M1 6.5 5 10.5 13 1.5" fill="none" stroke="#16b2a3" stroke-width="2.6" stroke-linecap="round" stroke-linejoin="round"/></svg><span>Minimized radiation exposure<br>with optimized protocols.</span></div>
  <div class="abs check-item" style="left:922px;top:724px;"><svg width="14" height="12" viewBox="0 0 14 12"><path d="M1 6.5 5 10.5 13 1.5" fill="none" stroke="#16b2a3" stroke-width="2.6" stroke-linecap="round" stroke-linejoin="round"/></svg><span>Experienced nuclear medicine<br>specialists.</span></div>

  <svg class="abs" style="left:1163px;top:670px" width="22" height="76" viewBox="0 0 22 76">
    <g fill="#16b2a3">
      <polygon points="11,0 22,12 0,12"/><polygon points="11,21 22,33 0,33"/>
      <polygon points="11,42 22,54 0,54"/><polygon points="11,63 22,75 0,75"/>
    </g>
  </svg>

</div>
</body>
</html>
```